Local 2D Joint Optical Promotion Flyer

A flyer to give to a customer group promoting two optical New York City offices and enticing members to come in and use their optical benefits. Flyer should promote use of benefits at our offices and bring covered patients in for exams and eyewear. We will offer $25 off in addition to covered benefits on the flyer.

Target Market(s)

Eye exam and eyeglass customers with covered benefits usable at our offices.

Industry/Entity Type

Group

Requirements
Must have
• Our businesses address and contact info, expiration date of March 31, 2017, ability to update the expiration date on my own, ability to change the group name on my own. Also must be able to have a black and white version along with the color version. Our two logos are attached, as well as a blank logo. Also, the previous flyer we were using is attached as the plmx2d file.
Nice to have
• Visual enticement to come in to our offices and use their coverage

```html
<!DOCTYPE html>
<html lang="en">
<head>
<meta charset="utf-8">
<title>Eye Glasses Benefit Flyer – Color and Black &amp; White</title>
<link rel="stylesheet" href="https://fonts.googleapis.com/css2?family=Nunito:wght@700;800&family=Open+Sans:wght@300;400;700;800&family=Raleway:wght@300;400&display=swap">
<style>
  :root{
    --stage:#b9b9b9;
    --accent:#5a9fd8;
    --accent-band:#4ea4ec;
    --ink:#4d4d4d;
    --text:#333;
    --paper:#f7f7f8;
    --box:#ececec;
    --coupon:#1c1c1c;
    --photo-a:#d9c2b6;
    --photo-b:#efe6e1;
  }
  html,body{margin:0;padding:0;overflow:hidden}
  body{
    width:1200px;height:847px;
    background:radial-gradient(ellipse at center,#d6d6d6 0%,var(--stage) 70%,#9f9f9f 100%);
    position:relative;font-family:"Open Sans",Arial,sans-serif;
  }
  .flyer{
    position:absolute;top:113px;width:492px;height:621px;
    background:var(--paper);overflow:hidden;color:var(--text);
    box-shadow:0 2px 8px rgba(0,0,0,.25);
  }
  .flyer--color{left:74px}
  .flyer--mono{
    left:649px;
    --accent:#8e8e8e;
    --accent-band:#9d9d9d;
    --photo-a:#bdbdbd;
    --photo-b:#e7e7e7;
  }
  .flyer__photo{
    position:absolute;left:0;top:0;width:300px;height:465px;
    background:linear-gradient(90deg,var(--photo-a) 0%,var(--photo-b) 55%,var(--paper) 100%);
  }
  .flyer__group{
    position:absolute;right:32px;top:28px;text-align:right;
    font-family:"Nunito",sans-serif;color:var(--accent);line-height:1.05;
  }
  .flyer__group-name{font-size:24px;font-weight:800;margin:0}
  .flyer__group-sub{font-size:19px;font-weight:700;margin:2px 0 0;font-family:"Open Sans",sans-serif;font-weight:400;letter-spacing:.3px}
  .benefit{position:absolute;left:246px;width:232px;top:101px;text-align:center;color:var(--ink)}
  .benefit__year{font-family:"Raleway",sans-serif;font-size:18px;font-weight:400;margin:0;line-height:1.1}
  .benefit__title{font-family:"Nunito",sans-serif;font-size:22px;font-weight:700;margin:0;line-height:1.15;letter-spacing:.2px}
  .benefit__rule{position:absolute;left:266px;top:149px}
  .entitled{position:absolute;left:228px;top:172px;width:250px}
  .entitled__heading{font-size:9.6px;font-weight:700;color:var(--accent);margin:0 0 8px;line-height:1.2}
  .entitled__list{list-style:none;margin:0;padding:0}
  .entitled__item{position:relative;padding-left:18px;font-size:7.6px;line-height:1.25;margin-bottom:7px}
  .entitled__item::before{content:"";position:absolute;left:0;top:2px;width:9px;height:9px;border-radius:50%;background:var(--accent)}
  .office{position:absolute;left:150px;width:310px;height:72px}
  .office--first{top:282px}
  .office--second{top:362px;height:77px}
  .office__brand{position:absolute;left:0;top:22px;width:94px;text-align:center;font-size:10px;color:#333;border-bottom:1px solid var(--accent);padding-bottom:3px}
  .office__dot{display:block;width:14px;height:14px;border-radius:50%;background:var(--accent);margin:0 auto 5px}
  .office__details{
    position:absolute;left:110px;top:0;right:0;bottom:0;background:var(--box);
    border-radius:3px;padding:5px 8px 0 18px;font-size:6.9px;line-height:8.7px;color:#444;
  }
  .office__details::before{content:"";position:absolute;left:0;top:0;bottom:0;width:1px;background:var(--accent)}
  .office__details::after{content:"";position:absolute;left:0;top:32px;border:4px solid transparent;border-left-color:var(--accent)}
  .office__details p{margin:0}
  .call-band{
    position:absolute;left:0;top:465px;width:100%;height:41px;
    background:linear-gradient(180deg,var(--accent-band),var(--accent-band) 70%,rgba(0,0,0,.05));
    background-color:var(--accent-band);
    color:#fff;font-weight:700;font-size:14.5px;text-align:center;line-height:40px;margin:0;
  }
  .coupon{position:absolute;left:0;top:506px;width:100%;height:115px;background:linear-gradient(180deg,#111,#2b2b2b)}
  .coupon__cut{position:absolute;left:0;top:3px;width:100%;border-top:1px dashed #ddd}
  .coupon__amount{position:absolute;left:40px;top:6px;color:var(--accent);font-weight:800;font-size:58px;line-height:1;letter-spacing:-2px}
  .coupon__amount sup{font-size:26px;vertical-align:top;position:relative;top:6px;margin-right:1px}
  .coupon__off{position:absolute;left:94px;top:56px;color:#fff;font-weight:300;font-size:42px;line-height:1}
  .coupon__divider{position:absolute;left:195px;top:28px;width:1px;height:56px;background:#fff}
  .coupon__divider::after{content:"";position:absolute;left:0;top:24px;border:4px solid transparent;border-left-color:#fff}
  .coupon__body{position:absolute;left:219px;top:16px;width:262px;color:#fff}
  .coupon__heading{font-family:"Nunito",sans-serif;font-size:17px;font-weight:800;color:var(--accent);margin:0 0 5px}
  .coupon__offer{font-size:11.2px;font-weight:700;line-height:13.5px;margin:0 0 6px}
  .coupon__terms,.coupon__expiry{font-size:6.8px;line-height:8.4px;margin:0}
  .coupon__expiry{margin-top:7px}
</style>
</head>
<body>

<article class="flyer flyer--color">
  <div class="flyer__photo" role="img" aria-label="Close-up portrait of a woman wearing black-framed eyeglasses"></div>
  <header class="flyer__group">
    <h1 class="flyer__group-name">Local 9 Riggers</h1>
    <p class="flyer__group-sub">Members &amp; Dependents</p>
  </header>
  <div class="benefit">
    <p class="benefit__year">Your 2016</p>
    <h2 class="benefit__title">Eye Glasses Benefit</h2>
  </div>
  <svg class="benefit__rule" width="192" height="12" viewBox="0 0 192 12"><rect x="0" y="2" width="192" height="2" fill="var(--accent)"/><path d="M88 4 L96 11 L104 4 Z" fill="var(--accent)"/></svg>
  <section class="entitled">
    <h3 class="entitled__heading">What You Are Entitled To At Birch Optical and Harlow and Finch Eyecare at NO COST To You:</h3>
    <ul class="entitled__list">
      <li class="entitled__item">A thorough and professional eye examination<br>checking both eye health and vision</li>
      <li class="entitled__item">A Wide Selection of frames fully covered by your plan</li>
      <li class="entitled__item">Standard eye glass lenses customized to your<br>prescription</li>
    </ul>
  </section>
  <section class="office office--first">
    <div class="office__brand"><span class="office__dot"></span>Birch Optical Group</div>
    <div class="office__details">
      <p>214 Lantern Avenue, 3rd Floor</p><p>Between Elm &amp; Oak Streets</p><p>(212) 555-0148</p><p>www.birchopticalgroup.com</p><p>Business Hours:</p><p>Monday and Wednesday 9:30am - 6pm</p><p>Tuesday, Thursday, and Friday 9:30am - 5:30pm</p>
    </div>
  </section>
  <section class="office office--second">
    <div class="office__brand"><span class="office__dot"></span>Harlow &amp; Finch Eyecare</div>
    <div class="office__details">
      <p>560 Quarry Avenue</p><p>Between Pine and Cedar Streets</p><p>(212) 555-0172</p><p>www.harlowfincheye.com</p><p>Business Hours:</p><p>Monday &amp; Thursday 9:30am - 7pm</p><p>Tuesday, Wednesday, &amp; Friday 9:30am - 6pm</p><p>Saturday 9:30am - 1pm</p>
    </div>
  </section>
  <p class="call-band">Call 212-555-0148 or 212-555-0172 for an appointment</p>
  <section class="coupon">
    <div class="coupon__cut"></div>
    <div class="coupon__amount"><sup>$</sup>25</div>
    <div class="coupon__off">OFF</div>
    <div class="coupon__divider"></div>
    <div class="coupon__body">
      <h3 class="coupon__heading">A Special Offer Just For You!</h3>
      <p class="coupon__offer">This Coupon Entitles You To $25 Off Any<br>Purchase Beyond Covered Allowance.</p>
      <p class="coupon__terms">Upon the use of your optical benefits at your next visit at either of<br>our 2 locations.</p>
      <p class="coupon__expiry">Expires 6/1/17.</p>
    </div>
  </section>
</article>

<article class="flyer flyer--mono">
  <div class="flyer__photo" role="img" aria-label="Black and white close-up portrait of a woman wearing black-framed eyeglasses"></div>
  <header class="flyer__group">
    <h1 class="flyer__group-name">Local 9 Riggers</h1>
    <p class="flyer__group-sub">Members &amp; Dependents</p>
  </header>
  <div class="benefit">
    <p class="benefit__year">Your 2016</p>
    <h2 class="benefit__title">Eye Glasses Benefit</h2>
  </div>
  <svg class="benefit__rule" width="192" height="12" viewBox="0 0 192 12"><rect x="0" y="2" width="192" height="2" fill="var(--accent)"/><path d="M88 4 L96 11 L104 4 Z" fill="var(--accent)"/></svg>
  <section class="entitled">
    <h3 class="entitled__heading">What You Are Entitled To At Birch Optical and Harlow and Finch Eyecare at NO COST To You:</h3>
    <ul class="entitled__list">
      <li class="entitled__item">A thorough and professional eye examination<br>checking both eye health and vision</li>
      <li class="entitled__item">A Wide Selection of frames fully covered by your plan</li>
      <li class="entitled__item">Standard eye glass lenses customized to your<br>prescription</li>
    </ul>
  </section>
  <section class="office office--first">
    <div class="office__brand"><span class="office__dot"></span>Birch Optical Group</div>
    <div class="office__details">
      <p>214 Lantern Avenue, 3rd Floor</p><p>Between Elm &amp; Oak Streets</p><p>(212) 555-0148</p><p>www.birchopticalgroup.com</p><p>Business Hours:</p><p>Monday and Wednesday 9:30am - 6pm</p><p>Tuesday, Thursday, and Friday 9:30am - 5:30pm</p>
    </div>
  </section>
  <section class="office office--second">
    <div class="office__brand"><span class="office__dot"></span>Harlow &amp; Finch Eyecare</div>
    <div class="office__details">
      <p>560 Quarry Avenue</p><p>Between Pine and Cedar Streets</p><p>(212) 555-0172</p><p>www.harlowfincheye.com</p><p>Business Hours:</p><p>Monday &amp; Thursday 9:30am - 7pm</p><p>Tuesday, Wednesday, &amp; Friday 9:30am - 6pm</p><p>Saturday 9:30am - 1pm</p>
    </div>
  </section>
  <p class="call-band">Call 212-555-0148 or 212-555-0172 for an appointment</p>
  <section class="coupon">
    <div class="coupon__cut"></div>
    <div class="coupon__amount"><sup>$</sup>25</div>
    <div class="coupon__off">OFF</div>
    <div class="coupon__divider"></div>
    <div class="coupon__body">
      <h3 class="coupon__heading">A Special Offer Just For You!</h3>
      <p class="coupon__offer">This Coupon Entitles You To $25 Off Any<br>Purchase Beyond Covered Allowance.</p>
      <p class="coupon__terms">Upon the use of your optical benefits at your next visit at either of<br>our 2 locations.</p>
      <p class="coupon__expiry">Expires 6/1/17.</p>
    </div>
  </section>
</article>

</body>
</html>
```